Supplement Bottle Label Design and Creative Lifestyle Images

We are a medical home consumer brand and we are releasing a supplement line of products called "Veltora Nutrition". We are in need of a supplement bottle design for our supplement line, Veltora Nutrition. We are looking for a very appealing, simple, and clean design, but with a medical feel to it.

We would like to see designs with a black background as well as designs with a white background. Bottle size will approximately be 200cc and label will about be 7" x 2.5", but this size is subject to change.

We really like the Prale Nutrition design and the Orvane Fieldworks, however, we like the medical style of Nutrition Bramwick. Please reference the links below.

To start off, the title of this bottle will be "Lumi-Vanta". We will need all similar warning about KRB, made in USA, non-GMA, GMP, ect. Please use the formula below to start:

2 Pills per serving
Blueberry pterostilbene - 10mg
Bacopa - 150mg
Gingko Biloba - 50mg
Vinpocetine - 10mg
Alpha-GPC -150mg
TAU - 35mg

https://www.brindlemart.example/Prale-Nutrition/b/ref=bl_dp_s_web_48203917725?ie=UTF8&node=48203917725&field-lbr_brands_browse-bin=Prale+Nutrition

https://www.brindlemart.example/l/7392058146

https://www.brindlemart.example/Nutrition-Bramwick/b/ref=bl_dp_s_web_61837405292?ie=UTF8&node=61837405292&field-lbr_brands_browse-bin=Nutrition+Bramwick

Medical

```html
<!DOCTYPE html>
<html lang="en">
<head>
<meta charset="utf-8">
<title>Veltora Nutrition – Lumi-Vanta Label</title>
<link rel="stylesheet" href="https://fonts.googleapis.com/css2?family=Exo+2:wght@600&family=Orbitron:wght@900&family=Saira+Condensed:wght@400;500;600&display=swap">
<style>
  :root{
    --canvas:#ffffff;
    --brand-blue:#1fa8e8;
    --sky:#6fd0f7;
    --band-dark:#26282c;
    --panel-dark:#141518;
    --tag-green:#4aa83a;
    --ingredient-orange:#f08a1c;
    --dose-grey:#b9bcc0;
    --text-light:#e9ecef;
  }
  *{box-sizing:border-box;margin:0;padding:0}
  html,body{width:1200px;height:950px;overflow:hidden;background:var(--canvas)}
  .sheet{position:relative;width:1200px;height:950px}
  .label{position:absolute;top:125px;width:540px;height:700px;overflow:hidden;border-radius:6px}
  .label--white{left:40px;--label-bg:#f3f4f5;--ring-a:#e6e8ea;--ring-b:#c3c6cb;--brain:#7cc8ef}
  .label--black{left:620px;--label-bg:#0d0e10;--ring-a:#3a3d42;--ring-b:#141518;--brain:#1c6fa8}
  .label__art{position:absolute;inset:0;width:540px;height:700px}
  .label__emblem{position:absolute;left:40px;top:112px;width:236px;height:236px}
  .brand{position:absolute;top:18px;left:170px;width:300px;text-align:center}
  .brand__name{font-family:"Exo 2",sans-serif;font-weight:600;font-size:46px;line-height:1;color:var(--brand-blue)}
  .brand__line{font-family:"Saira Condensed",sans-serif;font-weight:500;font-size:22px;letter-spacing:9px;color:var(--text-light);margin-top:4px}
  .supplement-tag{position:absolute;top:268px;left:338px;width:202px;height:48px;background:var(--tag-green);
    font-family:"Saira Condensed",sans-serif;font-size:23px;color:#fff;line-height:48px;padding-left:12px;white-space:nowrap}
  .product-title{position:absolute;top:344px;left:40px;font-family:"Orbitron",sans-serif;font-weight:900;font-size:46px;line-height:52px;color:var(--brand-blue);letter-spacing:1px}
  .ingredients{position:absolute;top:342px;left:394px;width:136px;list-style:none;font-family:"Saira Condensed",sans-serif}
  .ingredients li{display:flex;justify-content:space-between;align-items:flex-end;height:36px;font-size:14px;letter-spacing:1px;color:var(--ingredient-orange);line-height:1.05}
  .ingredients .dose{font-size:11px;color:var(--dose-grey);letter-spacing:0}
  .badges{position:absolute;top:462px;left:40px;display:flex;gap:12px;list-style:none}
  .badges li{width:62px;text-align:center;font-family:"Saira Condensed",sans-serif;font-weight:600;font-size:11px;color:var(--brand-blue);white-space:nowrap}
  .badges .badge-mark{display:block;width:42px;height:42px;margin:0 auto 4px;border:3px solid var(--brand-blue);border-radius:50%}
  .serving-info{position:absolute;top:634px;left:12px;font-family:"Saira Condensed",sans-serif;font-weight:600;color:var(--text-light);font-size:14px;line-height:16px}
  .serving-info .small{font-size:11px;color:var(--sky)}
  .net-weight{position:absolute;top:648px;right:16px;font-family:"Saira Condensed",sans-serif;font-weight:500;font-size:26px;line-height:30px;color:var(--sky)}
</style>
</head>
<body>
<main class="sheet">

  <section class="label label--white" aria-label="Lumi-Vanta label, white version">
    <svg class="label__art" viewBox="0 0 540 700" aria-hidden="true">
      <defs>
        <linearGradient id="skyW" x1="0" x2="1"><stop offset="0" stop-color="#1c8fd4"/><stop offset="1" stop-color="#8fdcfb"/></linearGradient>
      </defs>
      <rect width="540" height="700" fill="var(--label-bg)"/>
      <path d="M0 0H540V62Q300 128 0 86Z" fill="var(--band-dark)"/>
      <path d="M0 22Q140 40 250 112Q110 98 0 86Z" fill="url(#skyW)"/>
      <path d="M10 330H540V560H10Q20 445 10 330Z" fill="var(--panel-dark)"/>
      <line x1="384" y1="342" x2="384" y2="540" stroke="#3d4045" stroke-width="1"/>
      <path d="M0 600Q250 555 540 562V620H0Z" fill="url(#skyW)"/>
      <path d="M0 620Q260 590 540 596V700H0Z" fill="var(--band-dark)"/>
    </svg>
    <svg class="label__emblem" viewBox="0 0 236 236" role="img" aria-label="Brush-stroke ring framing a blue network brain illustration">
      <defs><radialGradient id="ringW"><stop offset="0" stop-color="var(--ring-a)"/><stop offset="1" stop-color="var(--ring-b)"/></radialGradient></defs>
      <circle cx="118" cy="118" r="114" fill="url(#ringW)"/>
      <ellipse cx="124" cy="118" rx="78" ry="58" fill="var(--brain)" opacity=".5"/>
    </svg>
    <div class="brand"><p class="brand__name">Veltora</p><p class="brand__line">NUTRITION</p></div>
    <p class="supplement-tag">Diatary Supplement</p>
    <h1 class="product-title">LUMI-<br>VANTA</h1>
    <ul class="ingredients">
      <li><span>BLUEBERRY<br>PTEROSTILBENE</span><span class="dose">10MG</span></li>
      <li><span>BACOPA</span><span class="dose">150MG</span></li>
      <li><span>GINGKO BILOBA</span><span class="dose">50MG</span></li>
      <li><span>VINPOCETINE</span><span class="dose">10MG</span></li>
      <li><span>ALPHA-GPC</span><span class="dose">150MG</span></li>
    </ul>
    <ul class="badges">
      <li><span class="badge-mark"></span>NON GMO</li>
      <li><span class="badge-mark"></span>GLUTEN FREE</li>
      <li><span class="badge-mark"></span>DIARY FREE</li>
      <li><span class="badge-mark"></span>SOY FREE</li>
    </ul>
    <p class="serving-info">115 CALORIES<br>30 SERVINGS<br><span class="small">2 PILLS/SERVING</span></p>
    <p class="net-weight">NET WT 990 g. | 2.18 LB</p>
  </section>

  <section class="label label--black" aria-label="Lumi-Vanta label, black version">
    <svg class="label__art" viewBox="0 0 540 700" aria-hidden="true">
      <defs>
        <linearGradient id="skyB" x1="0" x2="1"><stop offset="0" stop-color="#1c8fd4"/><stop offset="1" stop-color="#8fdcfb"/></linearGradient>
      </defs>
      <rect width="540" height="700" fill="var(--label-bg)"/>
      <path d="M0 0H540V62Q300 128 0 86Z" fill="var(--band-dark)"/>
      <path d="M0 22Q140 40 250 112Q110 98 0 86Z" fill="url(#skyB)"/>
      <path d="M10 330H540V560H10Q20 445 10 330Z" fill="var(--panel-dark)"/>
      <line x1="384" y1="342" x2="384" y2="540" stroke="#3d4045" stroke-width="1"/>
      <path d="M0 600Q250 555 540 562V620H0Z" fill="url(#skyB)"/>
      <path d="M0 620Q260 590 540 596V700H0Z" fill="var(--band-dark)"/>
    </svg>
    <svg class="label__emblem" viewBox="0 0 236 236" role="img" aria-label="Brush-stroke ring framing a blue network brain illustration">
      <defs><radialGradient id="ringB"><stop offset="0" stop-color="var(--ring-a)"/><stop offset="1" stop-color="var(--ring-b)"/></radialGradient></defs>
      <circle cx="118" cy="118" r="114" fill="url(#ringB)"/>
      <ellipse cx="124" cy="118" rx="78" ry="58" fill="var(--brain)" opacity=".6"/>
    </svg>
    <div class="brand"><p class="brand__name">Veltora</p><p class="brand__line">NUTRITION</p></div>
    <p class="supplement-tag">Diatary Supplement</p>
    <h1 class="product-title">LUMI-<br>VANTA</h1>
    <ul class="ingredients">
      <li><span>BLUEBERRY<br>PTEROSTILBENE</span><span class="dose">10MG</span></li>
      <li><span>BACOPA</span><span class="dose">150MG</span></li>
      <li><span>GINGKO BILOBA</span><span class="dose">50MG</span></li>
      <li><span>VINPOCETINE</span><span class="dose">10MG</span></li>
      <li><span>ALPHA-GPC</span><span class="dose">150MG</span></li>
    </ul>
    <ul class="badges">
      <li><span class="badge-mark"></span>NON GMO</li>
      <li><span class="badge-mark"></span>GLUTEN FREE</li>
      <li><span class="badge-mark"></span>DIARY FREE</li>
      <li><span class="badge-mark"></span>SOY FREE</li>
    </ul>
    <p class="serving-info">115 CALORIES<br>30 SERVINGS<br><span class="small">2 PILLS/SERVING</span></p>
    <p class="net-weight">NET WT 990 g. | 2.18 LB</p>
  </section>

</main>
</body>
</html>
```